Software Development Consulting Company Needs Business Card Design

We need a new business card design for our consultants at Marendo Solutions (marendosolutions.example). We are a small firm that provides high-end software development and methodology consulting to medium to large enterprise IT organizations.

Our logo uses Futura for the font and we would like to stick with navy blue and canary yellow for the logo colors. Attached are normal and reversed versions of our logos in illustrator format.
Updates

Hi Everyone, Thank yo very much for your amazing design ideas. I have created a poll for this project and our employees will be voting on the design they wish to use. We will be making a decision this Wednesday (October 22nd). Thanks again, Gavin Hartwell

Industry/Entity Type

Business

```html
<!DOCTYPE html>
<html lang="en">
<head>
<meta charset="utf-8">
<title>Marendo Solutions — Business Card</title>
<link rel="stylesheet" href="https://fonts.googleapis.com/css2?family=Lato:wght@400;700&display=swap">
<style>
  :root {
    --navy: #1d3f63;
    --navy-deep: #163352;
    --navy-light: #2e5678;
    --canary: #f7d117;
    --paper: #f2f2f1;
    --ink: #2a2a2a;
    --backdrop: #e4e4e3;
    --name-light: #dfe2e6;
  }
  * { margin: 0; padding: 0; box-sizing: border-box; }
  html, body { width: 1200px; height: 720px; overflow: hidden; }
  body {
    background: var(--backdrop);
    font-family: "Lato", sans-serif;
    position: relative;
  }
  .card {
    position: absolute;
    top: 242px;
    width: 420px;
    height: 238px;
    overflow: hidden;
  }
  .card-front { left: 147px; background: var(--paper); }
  .card-back {
    left: 633px;
    background: linear-gradient(135deg, var(--navy-light) 0%, var(--navy) 50%, var(--navy-deep) 100%);
  }

  /* Front */
  .name-band {
    position: absolute;
    left: 0; top: 70px;
    width: 100%; height: 51px;
    background: var(--navy);
    display: flex;
    align-items: center;
    justify-content: space-between;
    padding: 0 10px 0 37px;
    color: #fff;
    font-size: 19px;
    letter-spacing: 4.5px;
  }
  .band-mark {
    position: absolute;
    left: 50%; top: 50%;
    width: 14px; height: 14px;
    margin: -7px 0 0 -7px;
    border-radius: 50%;
    background: var(--canary);
  }
  .consultant {
    position: absolute;
    top: 153px; width: 100%;
    text-align: center;
    color: var(--navy);
  }
  .consultant-name { font-weight: 700; font-size: 13.5px; letter-spacing: -0.2px; }
  .consultant-title { font-size: 9.5px; color: var(--ink); }
  .contact-row {
    position: absolute;
    top: 196px; left: 0; width: 100%;
    display: flex;
    justify-content: center;
    align-items: center;
    font-size: 9.5px;
    color: var(--ink);
  }
  .contact-item { padding: 0 15px; line-height: 20px; }
  .contact-item + .contact-item { border-left: 1.5px solid var(--navy); }
  .footer-bar {
    position: absolute;
    left: 0; bottom: 0;
    width: 100%; height: 13px;
    background: var(--navy);
  }
  .footer-accent {
    position: absolute;
    left: 185px; top: 0;
    width: 49px; height: 100%;
    background: var(--canary);
  }

  /* Back */
  .company-name {
    position: absolute;
    top: 108px; left: 0; width: 100%;
    text-align: center;
    color: var(--name-light);
    font-size: 21px;
    font-weight: 400;
    letter-spacing: 5px;
    line-height: 1;
  }
  .web-address {
    position: absolute;
    bottom: 12px; width: 100%;
    text-align: center;
    font-size: 10px;
    color: #e6e6e6;
  }
  .web-address .domain { color: var(--canary); }
</style>
</head>
<body>
  <section class="card card-front" aria-label="Business card front">
    <div class="name-band">
      <span class="band-word">MARENDO</span>
      <span class="band-mark" aria-hidden="true"></span>
      <span class="band-word">SOLUTIONS</span>
    </div>
    <div class="consultant">
      <p class="consultant-name">Gavin Hartwell</p>
      <p class="consultant-title">Principal Consultant</p>
    </div>
    <div class="contact-row">
      <span class="contact-item">555-014-2387</span>
      <span class="contact-item">gavin.hartwell@marendosolutions.example</span>
      <span class="contact-item">@gavinhart</span>
    </div>
    <div class="footer-bar"><span class="footer-accent"></span></div>
  </section>

  <section class="card card-back" aria-label="Business card back">
    <p class="company-name">MARENDO SOLUTIONS</p>
    <p class="web-address">www.<span class="domain">marendosolutions</span>.example</p>
  </section>
</body>
</html>
```